New professional looking flyer for company

I need our flyer updated my flyer is the Lvb flyer Have attached current flyer so you know what services need to be listed. Want it to be in mainly dark colours like black and dark grey with pops of light grey, silver or white. i have added several photos for you to choose which ones work best with your design would like The photos to be in colour for the flyer. But can have a mix of greyscale if that works for your design j have attached another companies flyers as design ideas to show what I am looking for

Target Market(s)

new clients

Industry/Entity Type

transport and earthmoving

Colors

Designer to choose colors to be used in the design.

Requirements
Nice to have
• Look professional
Should not have
• No orange or red or green

```html
<!DOCTYPE html>
<html lang="en">
<head>
<meta charset="utf-8">
<title>Lvb Pty Ltd – Our Services Flyer</title>
<link rel="stylesheet" href="https://fonts.googleapis.com/css2?family=Poppins:wght@500;600;800&family=Oswald:wght@600&display=swap">
<style>
:root{
  --page:#ffffff;
  --ink-900:#111111;
  --ink-800:#1b1b1b;
  --ink-700:#262626;
  --ink-600:#333333;
  --silver-100:#f1f1f1;
  --silver-300:#c9c9c9;
  --silver-500:#8e8e8e;
  --white:#ffffff;
  --rule:#5a5a5a;
}
*{margin:0;padding:0;box-sizing:border-box}
html,body{width:1200px;height:2457px;overflow:hidden;background:var(--page)}
.flyer{
  position:absolute;left:50px;top:516px;width:1100px;height:1425px;
  background:radial-gradient(ellipse at 50% 15%,var(--ink-700),var(--ink-900) 70%);
  overflow:hidden;font-family:"Poppins",sans-serif;color:var(--white);
  box-shadow:0 18px 40px rgba(0,0,0,.35);
}
.brand{position:absolute;left:0;right:0;top:53px;text-align:center}
.brand-rule{position:absolute;left:345px;width:410px;height:2px;background:var(--silver-500)}
.brand-rule.top{top:0}
.brand-name{display:block;padding-top:14px;font-weight:800;font-size:150px;line-height:1;color:var(--silver-300);letter-spacing:4px}
.brand-sub{display:flex;align-items:center;justify-content:center;gap:22px;margin-top:10px;font-weight:800;font-size:36px;color:var(--silver-300)}
.brand-sub::before,.brand-sub::after{content:"";width:130px;height:2px;background:var(--silver-500)}
.hero-photo{
  position:absolute;left:0;top:306px;width:1100px;height:210px;
  background:linear-gradient(180deg,#cfd6dc 0%,#e9e9e6 35%,#8a7a62 75%,#5e4d3a 100%);
  clip-path:polygon(0 18%,8% 10%,18% 16%,30% 6%,45% 14%,60% 4%,72% 12%,85% 3%,100% 10%,100% 100%,0 100%);
}
.services-band{
  position:absolute;left:0;top:516px;width:1100px;height:131px;
  background:linear-gradient(90deg,var(--silver-500),var(--silver-100) 50%,var(--silver-500));
}
.services-band svg{position:absolute;left:0;top:0}
.services-title{
  position:absolute;left:0;right:0;top:18px;text-align:center;
  font-weight:800;font-size:92px;line-height:1;color:var(--silver-300);letter-spacing:1px;
}
.service-list{position:absolute;left:56px;top:690px;width:620px;list-style:none}
.service-list li{
  display:flex;align-items:flex-start;gap:14px;font-weight:500;font-size:27px;line-height:32px;
  padding:8px 0 8px 0;border-bottom:2px solid var(--rule);
}
.service-list li:last-child{border-bottom:none}
.service-list svg{flex:none;margin-top:7px}
.tab{
  position:absolute;left:688px;top:664px;width:412px;height:39px;
  background:linear-gradient(90deg,var(--silver-300),var(--silver-100));
  color:var(--ink-800);font-weight:600;font-size:25px;line-height:39px;padding-left:34px;letter-spacing:.5px;
}
.job-photo{
  position:absolute;left:658px;width:401px;height:154px;
  clip-path:polygon(6% 0,100% 0,94% 100%,0 100%);
  border:none;
}
.job-photo.p1{top:719px;background:linear-gradient(160deg,#5c7fb8 0%,#9aa3aa 45%,#6a5a48 100%)}
.job-photo.p2{top:888px;background:linear-gradient(160deg,#4f79c2 0%,#7c7a73 45%,#8a4a30 100%)}
.job-photo.p3{top:1055px;background:linear-gradient(160deg,#8fa4c2 0%,#b8b3ab 45%,#6b5c4d 100%)}
.job-photo.p4{top:1224px;background:linear-gradient(180deg,#3b72c8 0%,#8db0de 45%,#a2522e 100%)}
.photo-edge{position:absolute;left:880px;top:1150px;width:220px;height:275px;
  background:linear-gradient(160deg,transparent 40%,var(--silver-500));opacity:.5}
.offer-bar{
  position:absolute;left:0;top:1165px;width:616px;height:68px;
  background:linear-gradient(90deg,var(--silver-500),var(--silver-100) 60%,var(--silver-300));
  display:flex;align-items:center;padding-left:54px;color:var(--ink-900);
}
.offer-title{font-family:"Oswald",sans-serif;font-weight:600;font-size:46px;line-height:1}
.offer-divider{width:3px;height:44px;background:var(--ink-900);margin:0 22px}
.offer-note{font-weight:600;font-size:19px;line-height:22px}
.cta{position:absolute;left:58px;top:1255px;font-weight:500;font-size:32px;line-height:40px}
.contacts{position:absolute;left:54px;top:1350px;display:flex;gap:28px;font-weight:500;font-size:18px;align-items:center}
.contacts span{display:flex;align-items:center;gap:8px}
</style>
</head>
<body>
<main class="flyer">
  <header class="brand">
    <div class="brand-rule top"></div>
    <span class="brand-name">Lvb</span>
    <div class="brand-sub">Pty Ltd</div>
  </header>

  <div class="hero-photo" role="img" aria-label="Photograph of a white road train with water tanker trailers parked on a red dirt site"></div>

  <section class="services-band">
    <svg width="1100" height="131" viewBox="0 0 1100 131" aria-hidden="true">
      <path d="M160 20 L960 8 L940 40 L990 60 L930 90 L950 122 L150 128 L175 95 L120 70 L170 45 Z" fill="#141414"/>
    </svg>
    <h1 class="services-title">OUR SERVICES</h1>
  </section>

  <ul class="service-list">
    <li><svg width="18" height="18" viewBox="0 0 18 18"><circle cx="9" cy="9" r="7.5" fill="none" stroke="#fff" stroke-width="1.6"/><path d="M5.5 9.2l2.4 2.3 4.6-4.8" fill="none" stroke="#fff" stroke-width="1.6"/></svg>Over size loads / Hot Shot Loads</li>
    <li><svg width="18" height="18" viewBox="0 0 18 18"><circle cx="9" cy="9" r="7.5" fill="none" stroke="#fff" stroke-width="1.6"/><path d="M5.5 9.2l2.4 2.3 4.6-4.8" fill="none" stroke="#fff" stroke-width="1.6"/></svg>Heavy Vehicle Recovery Services</li>
    <li><svg width="18" height="18" viewBox="0 0 18 18"><circle cx="9" cy="9" r="7.5" fill="none" stroke="#fff" stroke-width="1.6"/><path d="M5.5 9.2l2.4 2.3 4.6-4.8" fill="none" stroke="#fff" stroke-width="1.6"/></svg>Potable Water Deliveries</li>
    <li><svg width="18" height="18" viewBox="0 0 18 18"><circle cx="9" cy="9" r="7.5" fill="none" stroke="#fff" stroke-width="1.6"/><path d="M5.5 9.2l2.4 2.3 4.6-4.8" fill="none" stroke="#fff" stroke-width="1.6"/></svg>Road Building / Maintenance</li>
    <li><svg width="18" height="18" viewBox="0 0 18 18"><circle cx="9" cy="9" r="7.5" fill="none" stroke="#fff" stroke-width="1.6"/><path d="M5.5 9.2l2.4 2.3 4.6-4.8" fill="none" stroke="#fff" stroke-width="1.6"/></svg>Earthworks</li>
    <li><svg width="18" height="18" viewBox="0 0 18 18"><circle cx="9" cy="9" r="7.5" fill="none" stroke="#fff" stroke-width="1.6"/><path d="M5.5 9.2l2.4 2.3 4.6-4.8" fill="none" stroke="#fff" stroke-width="1.6"/></svg>Sand &amp; Metal Supply &amp; Cartage</li>
    <li><svg width="18" height="18" viewBox="0 0 18 18"><circle cx="9" cy="9" r="7.5" fill="none" stroke="#fff" stroke-width="1.6"/><path d="M5.5 9.2l2.4 2.3 4.6-4.8" fill="none" stroke="#fff" stroke-width="1.6"/></svg>Road Train Tippers Road Train</li>
    <li><svg width="18" height="18" viewBox="0 0 18 18"><circle cx="9" cy="9" r="7.5" fill="none" stroke="#fff" stroke-width="1.6"/><path d="M5.5 9.2l2.4 2.3 4.6-4.8" fill="none" stroke="#fff" stroke-width="1.6"/></svg>Tankers Road Train Flat Tops Drop</li>
    <li><svg width="18" height="18" viewBox="0 0 18 18"><circle cx="9" cy="9" r="7.5" fill="none" stroke="#fff" stroke-width="1.6"/><path d="M5.5 9.2l2.4 2.3 4.6-4.8" fill="none" stroke="#fff" stroke-width="1.6"/></svg>Deck Trailers Mine Site accredited<br>equipment &amp; Operators</li>
  </ul>

  <div class="tab">TRAFFIC MANAGEMENT</div>
  <div class="photo-edge"></div>
  <div class="job-photo p1" role="img" aria-label="Photograph of a loader beside a tanker trailer with site workers in hi-vis"></div>
  <div class="job-photo p2" role="img" aria-label="Photograph of a truck and grader working on a red dirt road"></div>
  <div class="job-photo p3" role="img" aria-label="Photograph of a tipper trailer unloading crushed rock"></div>
  <div class="job-photo p4" role="img" aria-label="Photograph of a prime mover hauling a tanker across red desert ground"></div>

  <div class="offer-bar">
    <span class="offer-title">WE OFFER</span>
    <span class="offer-divider"></span>
    <span class="offer-note">A LARGE RANGE OF<br>SERVICES NOT LISTED SO</span>
  </div>

  <p class="cta">Call us Today for a personalised<br>quote to suit your needs.</p>

  <div class="contacts">
    <span><svg width="24" height="24" viewBox="0 0 24 24"><circle cx="12" cy="12" r="10.5" fill="none" stroke="#fff" stroke-width="1.6"/><path d="M8 7l2 0 1 3-1.3 1a6 6 0 0 0 3.3 3.3l1-1.3 3 1v2a1.5 1.5 0 0 1-1.7 1.3A9 9 0 0 1 6.7 8.7 1.5 1.5 0 0 1 8 7z" fill="#fff"/></svg>700 555 0142</span>
    <span><svg width="24" height="24" viewBox="0 0 24 24"><circle cx="12" cy="12" r="10.5" fill="none" stroke="#fff" stroke-width="1.6"/><rect x="6.5" y="8" width="11" height="8" fill="none" stroke="#fff" stroke-width="1.4"/><path d="M6.5 8l5.5 4.5L17.5 8" fill="none" stroke="#fff" stroke-width="1.4"/></svg>info@lvb.com.au</span>
    <span><svg width="24" height="24" viewBox="0 0 24 24"><circle cx="12" cy="12" r="10.5" fill="none" stroke="#fff" stroke-width="1.6"/><circle cx="12" cy="12" r="5.5" fill="none" stroke="#fff" stroke-width="1.3"/><path d="M6.5 12h11M12 6.5c-2.5 3-2.5 8 0 11M12 6.5c2.5 3 2.5 8 0 11" fill="none" stroke="#fff" stroke-width="1.1"/></svg>www.lvb.com.au</span>
  </div>
</main>
</body>
</html>
```